Professional Home Buyer business card needed

I need a pretty straight forward business card designed. We help people that NEED to sell their homes solve problems. We perform all types of Real Estate transactions including flip, wholesale, investment, rental property and multi family. The card will mainly be used to give to prospective Sellers but will also be given to Real Estate Investors as well. It should professional and very easy to read, most clients are older people.

Target Market(s)

Distressed home sellers as well as Real Estate investors

Industry/Entity Type

Real Estate

Contact Information for Business Card

should be a professional layout

Colors
ec1f27
ffffff
000000

Requirements
Must have
• Large logo on back and smaller one on front. should utilize Red, white, and black.
• I am thinking of using a soft touch coating on the card so keep that in mind.
• Contact info should be very easy to read, think older clients.
Nice to have
• I would like to see a design with rounded corners on the card
Should not have
• pictures of homes or other home graphics.

```html
<!DOCTYPE html>
<html lang="en">
<head>
<meta charset="utf-8">
<title>Brindlewick Home Buyers – Business Card</title>
<link rel="stylesheet" href="https://fonts.googleapis.com/css2?family=Roboto:wght@400;500;900&display=swap">
<style>
  :root {
    --brand-red: #ec1f27;
    --brand-white: #ffffff;
    --brand-black: #000000;
    --text-grey: #4a4a4a;
    --stage: #eeeeee;
  }
  * { box-sizing: border-box; margin: 0; padding: 0; }
  html, body {
    width: 1200px; height: 711px; overflow: hidden;
    background: var(--stage);
    font-family: "Roboto", Arial, sans-serif;
  }
  .sheet {
    width: 1200px; height: 711px;
    display: flex; align-items: center; justify-content: center; gap: 40px;
  }
  .card {
    width: 540px; height: 308px;
    border-radius: 10px;
    position: relative;
    box-shadow: 0 2px 6px rgba(0,0,0,.12);
    overflow: hidden;
  }
  .card--front { background: var(--brand-white); }
  .card--back {
    background: var(--brand-black);
    display: flex; align-items: center; justify-content: center;
  }

  /* Front */
  .brand { position: absolute; left: 36px; top: 32px; }
  .brand__tagline {
    font-size: 9px; font-weight: 500; letter-spacing: 3px;
    text-transform: uppercase; color: var(--brand-black);
    margin-bottom: 8px;
  }
  .brand__lockup { display: flex; align-items: center; gap: 10px; }
  .brand__mark { width: 18px; height: 18px; background: var(--brand-red); flex: none; }
  .brand__name {
    font-weight: 900; color: var(--brand-black);
    font-size: 28px; line-height: 1; letter-spacing: 1px;
    text-transform: uppercase;
  }
  .brand__name span { display: block; font-size: 15px; letter-spacing: 5px; margin-top: 5px; }

  .contact { position: absolute; left: 36px; bottom: 30px; color: var(--text-grey); }
  .contact__address { font-size: 13px; line-height: 1.35; margin-bottom: 10px; }
  .contact__list { list-style: none; font-size: 13px; line-height: 1.45; }
  .contact__list li { display: flex; align-items: center; gap: 8px; }
  .contact__icon { width: 11px; height: 11px; flex: none; fill: var(--brand-red); }

  .person { position: absolute; right: 40px; top: 132px; text-align: right; }
  .person__name {
    font-size: 17px; font-weight: 500; color: var(--brand-red);
    text-transform: uppercase; letter-spacing: .5px; line-height: 1.2;
  }
  .person__title {
    font-size: 12px; font-weight: 500; color: var(--brand-black);
    text-transform: uppercase;
  }

  /* Back */
  .brand--large { display: flex; align-items: center; gap: 18px; }
  .brand--large .brand__mark { width: 32px; height: 32px; }
  .brand--large .brand__name { color: var(--brand-white); font-size: 46px; }
</style>
</head>
<body>
<main class="sheet">
  <section class="card card--front" aria-label="Card front">
    <div class="brand">
      <p class="brand__tagline">Fair offers, fast close!</p>
      <div class="brand__lockup">
        <span class="brand__mark" aria-hidden="true"></span>
        <p class="brand__name">Brindlewick<span>Home Buyers</span></p>
      </div>
    </div>

    <div class="person">
      <p class="person__name">Daniel Reyes</p>
      <p class="person__title">CEO/Founder</p>
    </div>

    <div class="contact">
      <p class="contact__address">4120 Birchwood Court<br>Fairbanks, Alaska 34610</p>
      <ul class="contact__list">
        <li>
          <svg class="contact__icon" viewBox="0 0 12 12" aria-hidden="true"><path d="M2.5 1l2 2.5-1.2 1.2a7 7 0 0 0 4 4L8.5 7.5 11 9.5 9.8 11C5 11 1 7 1 2.2z"/></svg>
          555 201 4830
        </li>
        <li>
          <svg class="contact__icon" viewBox="0 0 12 12" aria-hidden="true"><path d="M3 0h6v12H3zM4 1.5v8h4v-8z"/></svg>
          555 318 7742
        </li>
        <li>
          <svg class="contact__icon" viewBox="0 0 12 12" aria-hidden="true"><path d="M3 0h6v3H3zM0 4h12v6H9v2H3v-2H0zM4 8v3h4V8z"/></svg>
          555 462 0915
        </li>
        <li>
          <svg class="contact__icon" viewBox="0 0 12 12" aria-hidden="true"><path d="M0 2h12v1L6 7 0 3zM0 4.5l6 4 6-4V10H0z"/></svg>
          daniel@brindlewickhb.example
        </li>
        <li>
          <svg class="contact__icon" viewBox="0 0 12 12" aria-hidden="true"><circle cx="6" cy="6" r="6"/></svg>
          www.brindlewickhb.example
        </li>
      </ul>
    </div>
  </section>

  <section class="card card--back" aria-label="Card back">
    <div class="brand--large">
      <span class="brand__mark" aria-hidden="true"></span>
      <p class="brand__name">Brindlewick</p>
    </div>
  </section>
</main>
</body>
</html>
```